Logo, Business Card & Stationery Design Project

Firstly, we need a quick turnaround for this project.
The company is KLT Financial.
KLT Financial specialises in sourcing, marketing and introducing clients to hassle free investment property opportunities. We are looking for a design representing stability, professionalism and customer focused. We also need to have the feel of being approachable and practical.
The design will be for the logo initially followed by business cards, letterhead (inc word based doc), with compliments, envelopes, stickers and Word documents for a letterhead & title page.
We look forward to seeing your designs.
Target Market(s)
Generally middle class couples aged from 30-50
Industry/Entity Type
Investment
Look and feel
Each slider illustrates characteristics of the customer's brand and the style your logo design should communicate.

```html
<!DOCTYPE html>
<html lang="en">
<head>
<meta charset="utf-8">
<title>KLT Financial – Business Card</title>
<link href="https://fonts.googleapis.com/css2?family=Montserrat:wght@300&display=swap" rel="stylesheet">
<style>
  :root {
    --page: #ffffff;
    --card: #261e0c;
    --stone: #bab2a6;
    --amber: #f29b1f;
  }
  html, body {
    margin: 0;
    padding: 0;
    width: 1200px;
    height: 900px;
    overflow: hidden;
    background: var(--page);
  }
  .canvas {
    position: relative;
    width: 1200px;
    height: 900px;
    background: var(--page);
  }
  .card {
    position: absolute;
    left: 0;
    top: 114px;
    width: 1200px;
    height: 672px;
    background: var(--card);
    font-family: "Montserrat", "Helvetica Neue", Arial, sans-serif;
    font-weight: 300;
  }
  .brand-mark {
    position: absolute;
    right: 75px;
    top: 226px;
    width: 152px;
    height: 152px;
    background: var(--amber);
  }
  .brand-name {
    position: absolute;
    right: 35px;
    top: 426px;
    margin: 0;
    font-size: 86px;
    font-weight: 300;
    line-height: 1;
    letter-spacing: 5px;
    color: var(--stone);
    white-space: nowrap;
  }
  .website {
    position: absolute;
    right: 66px;
    top: 595px;
    margin: 0;
    font-size: 27px;
    font-weight: 300;
    line-height: 1;
    letter-spacing: 2px;
    color: var(--amber);
    white-space: nowrap;
  }
</style>
</head>
<body>
  <div class="canvas">
    <section class="card">
      <div class="brand-mark" aria-hidden="true"></div>
      <h1 class="brand-name">KLT FINANCIAL</h1>
      <p class="website">WWW.KLTFINANCIAL.COM.AU</p>
    </section>
  </div>
</body>
</html>
```